METAL FABRICATION BUSINESS CARD

** I will be ending the project and picking design early. This Friday October 3rd at 7am MST if not sooner**
ONE SIDED BUSINESS CARD ONLY. AND LOGO SIZE TO BE DOMINANT so it stands out.
Looking for a black background and will be doing raised chrome/silver font on the business cards. Looking to have the following on the front of the business card. Company logo is uploaded in files.
Company logo
*Compartment Doors
*Roof Radius Metal
*J-Wrap Metal Skirting
*S-Lock Beltline Molding
*Pre-Bent Molding
and more...
Owen Daltry 307.552.4198 info@KX-Welt.com
Updates
One sided business card only please. Also logo size should be dominant and sized bigger
Contact Information for Business Card
Black background, Text will be raised chrome/silver, and corners will be rounded.

```html
<!DOCTYPE html>
<html lang="en">
<head>
<meta charset="utf-8">
<title>KX-Welt Business Card</title>
<link rel="stylesheet" href="https://fonts.googleapis.com/css2?family=Montserrat:wght@400;600;700&display=swap">
<style>
  :root {
    --backdrop: #9a9a9a;
    --card: #161616;
    --card-sheen: #2e2e2e;
    --silver: #e4e4e4;
    --silver-soft: #d6d6d6;
  }
  html, body {
    margin: 0;
    width: 1200px;
    height: 1108px;
    overflow: hidden;
    background: var(--backdrop);
    font-family: "Montserrat", sans-serif;
  }
  .card {
    position: absolute;
    left: 242px;
    width: 716px;
    height: 409px;
    border-radius: 26px;
    background: var(--card);
    color: var(--silver);
    overflow: hidden;
  }
  .card--front {
    top: 119px;
    background: linear-gradient(120deg, var(--card) 0%, var(--card) 38%, var(--card-sheen) 55%, var(--card) 85%);
  }
  .card--back { top: 581px; }

  .brand {
    position: absolute;
    display: flex;
    align-items: center;
    font-weight: 700;
    color: var(--silver);
    white-space: nowrap;
  }
  .brand__dot {
    border-radius: 50%;
    background: var(--silver);
    flex: none;
  }
  .card--front .brand {
    left: 0; right: 0; top: 0; bottom: 0;
    justify-content: center;
    gap: 22px;
    font-size: 104px;
    letter-spacing: -1px;
  }
  .card--front .brand__dot { width: 44px; height: 44px; }
  .card--back .brand {
    left: 28px;
    top: 44px;
    gap: 14px;
    font-size: 76px;
    letter-spacing: -1px;
  }
  .card--back .brand__dot { width: 30px; height: 30px; }

  .services {
    position: absolute;
    right: 28px;
    top: 176px;
    text-align: right;
  }
  .services__title {
    margin: 0 0 10px;
    font-size: 39px;
    font-weight: 700;
    line-height: 1;
    color: var(--silver-soft);
  }
  .services__list {
    list-style: none;
    margin: 0;
    padding: 0;
    font-size: 18.5px;
    line-height: 31.3px;
    letter-spacing: 0.4px;
  }

  .contact {
    position: absolute;
    left: 29px;
    top: 258px;
  }
  .contact__name {
    margin: 0 0 26px;
    font-size: 30px;
    font-weight: 600;
    line-height: 1.2;
    color: var(--silver-soft);
  }
  .contact__line {
    display: flex;
    align-items: center;
    gap: 10px;
    font-size: 18.5px;
    line-height: 31px;
    letter-spacing: 0.4px;
  }
  .contact__icon { width: 16px; height: 14px; fill: var(--silver); flex: none; }
</style>
</head>
<body>
  <section class="card card--front">
    <div class="brand"><span class="brand__dot"></span>KX-Welt</div>
  </section>

  <section class="card card--back">
    <div class="brand"><span class="brand__dot"></span>KX-Welt</div>

    <div class="services">
      <h2 class="services__title">OUR SERVICE</h2>
      <ul class="services__list">
        <li>Compartment Doors</li>
        <li>*Roof Radius Metal</li>
        <li>*J-Wrap Metal Skirting</li>
        <li>*S-Lock Beltline Molding</li>
        <li>*Pre-Bent Molding</li>
      </ul>
    </div>

    <div class="contact">
      <h1 class="contact__name">Owen Daltry</h1>
      <div class="contact__line">
        <svg class="contact__icon" viewBox="0 0 16 14" aria-hidden="true">
          <path d="M1 4 Q8 -1 15 4 L13 6 L10 4.5 L6 4.5 L3 6 Z"/>
          <rect x="3" y="7" width="10" height="6" rx="1"/>
        </svg>
        <span>307.552.4198</span>
      </div>
      <div class="contact__line">
        <svg class="contact__icon" viewBox="0 0 16 14" aria-hidden="true">
          <path d="M1 3 H15 V12 H1 Z M2 4 L8 8.5 L14 4" fill="none" stroke="#e4e4e4" stroke-width="1.5"/>
        </svg>
        <span>info@KX-Welt.com</span>
      </div>
    </div>
  </section>
</body>
</html>
```